Tavrel Software Overview Brochure

Tavrel Software has developed a cloud based accounting systems for small businesses that have out grown products like Brindlepath. We need an overview brochure that can be delivered in a PDF and become incorporated into our web site. I have attached our logo as a reference for colors and style.

The brochure should be speak to small business owners and communicate why Tavrel is better for them than Brindlepath. I will be happy to provide screen shots and content.

Target Market(s)

companies between 10 and 200 employees

Industry/Entity Type

Small Business

Requirements
Must have
• Strong branding around the Tavrel name and logo. Room for screen shots of the software and discussion of product features.

```html
<!DOCTYPE html>
<html lang="en">
<head>
<meta charset="utf-8">
<title>Tavrel Software – Small Business Management in the Cloud</title>
<link rel="stylesheet" href="https://fonts.googleapis.com/css2?family=Source+Sans+3:wght@400;600;700&display=swap">
<style>
  :root {
    --stage-grey: #a9a9a9;
    --paper: #ffffff;
    --charcoal: #3a3a3c;
    --brand-red: #be1e2d;
    --ink: #2b2b2b;
  }
  * { box-sizing: border-box; margin: 0; padding: 0; }
  html, body { width: 1200px; height: 1000px; overflow: hidden; }
  body {
    background: var(--stage-grey);
    font-family: "Source Sans 3", "Myriad Pro", Arial, sans-serif;
    position: relative;
  }
  .brochure-page {
    position: absolute;
    top: 91px;
    width: 580px;
    height: 822px;
    background: var(--paper);
    overflow: hidden;
  }
  .brochure-page--overview { left: 15px; }
  .brochure-page--upgrade { left: 603px; }

  .brand-lockup {
    position: absolute;
    top: 26px;
    right: 30px;
    display: flex;
    align-items: center;
    gap: 12px;
  }
  .brand-lockup__dot {
    width: 56px;
    height: 56px;
    border-radius: 50%;
    background: var(--brand-red);
  }
  .brand-lockup__name {
    color: var(--brand-red);
    font-size: 31px;
    font-weight: 600;
    letter-spacing: 0.5px;
  }

  .title-band {
    position: absolute;
    top: 105px;
    left: 0;
    width: 525px;
    height: 75px;
    background: var(--charcoal);
  }
  .title-band__pointer {
    position: absolute;
    left: 33px;
    bottom: -21px;
    width: 0;
    height: 0;
    border-left: 12px solid transparent;
    border-right: 12px solid transparent;
    border-top: 21px solid var(--charcoal);
  }
  .title-band__heading {
    position: absolute;
    left: 67px;
    top: 8px;
    color: #fff;
    font-size: 26px;
    line-height: 28px;
    font-weight: 700;
    text-shadow: 1px 1px 1px rgba(0,0,0,0.5);
  }
  .title-accent {
    position: absolute;
    top: 105px;
    left: 528px;
    width: 52px;
    height: 75px;
    background: var(--brand-red);
  }

  .page-copy {
    position: absolute;
    top: 192px;
    left: 67px;
    width: 448px;
    color: var(--ink);
    font-size: 11.6px;
    line-height: 21.7px;
    text-align: justify;
  }
  .page-copy p + p { margin-top: 21.7px; }

  .feature-list {
    list-style: none;
    counter-reset: feature;
  }
  .feature-list li {
    counter-increment: feature;
    position: relative;
    padding-left: 70px;
  }
  .feature-list li::before {
    content: counter(feature) ".";
    position: absolute;
    left: 35px;
  }

  .footer-band {
    position: absolute;
    left: 0;
    right: 0;
    top: 759px;
    height: 43px;
    background: var(--brand-red);
  }
</style>
</head>
<body>

<section class="brochure-page brochure-page--overview">
  <div class="brand-lockup">
    <span class="brand-lockup__dot"></span>
    <span class="brand-lockup__name">Tavrel Software</span>
  </div>
  <header class="title-band">
    <h1 class="title-band__heading">Small Business Management<br>in the Cloud</h1>
    <span class="title-band__pointer"></span>
  </header>
  <div class="title-accent"></div>
  <div class="page-copy">
    <p>Tavrel Software (Tavrel) is the first online business management application exclusively written for small businesses that is built on the Corvane Relate CRM platform. More than just accounting, Tavrel provides the necessary tools and processes to help businesses grow. Tavrel gets results not just numbers by incorporating many of the principles of KOS™ (Keystone Operating System www.keystoneos.com).</p>
    <p>Tavrel’s robust features are designed to leverage a company’s growth without holding it back. Our key design element provides a user-friendly interface while ensuring the integrity of a company’s data. Tavrel’s complete accounting audit trail provides a one click correction to any transaction. You can easily enter and manage a transaction on one screen. No popups or multiple clicks needed, e.g., you can enter a voucher, post it and print a check from one screen. So simple, yet powerful!</p>
    <p>Corvane Relate CRM platform hosts over 40,000 companies worldwide and has become one of the most reliable platforms available today. By utilizing Corvane Relate CRM Online cloud based platform, Tavrel makes it simple for businesses to operate from anywhere, at anytime.</p>
    <p>Companies have the distinct advantage of having one platform for CRM and Financials that are fully integrated to meet your unique business needs. There’s no need to manage two separate applications or install software to integrate CRM with your accounting application.</p>
  </div>
  <div class="footer-band"></div>
</section>

<section class="brochure-page brochure-page--upgrade">
  <div class="brand-lockup">
    <span class="brand-lockup__dot"></span>
    <span class="brand-lockup__name">Tavrel Software</span>
  </div>
  <header class="title-band">
    <h2 class="title-band__heading">Small Business Management<br>in the Cloud</h2>
    <span class="title-band__pointer"></span>
  </header>
  <div class="title-accent"></div>
  <div class="page-copy">
    <p>Simply and Easily Upgrade from Brindlepath™ for companies that have outgrown Brindlepath, Tavrel provides advanced features to grow your business efficiently. Tavrel’s business management features include:</p>
    <ol class="feature-list">
      <li>Dimension Reporting</li>
      <li>Multi-Location Inventory</li>
      <li>Full Role Based Security</li>
      <li>Complete Transaction Audit Trail</li>
      <li>Segmented Chart of Accounts</li>
    </ol>
    <p style="margin-top:0">Tavrel allows companies to move from Brindlepath as simple as following a wizard in less than an hour.</p>
  </div>
  <div class="footer-band"></div>
</section>

</body>
</html>
```